Modern Yoga Studio Timetable and Flyer Design

We have a comprehensive class timetable and we are wanting to a clean modern look for our Spring timetable.

We require a double sided flyer with our class timetable included.
We would prefer an A5 size (postcard) or DL (1/3 A4).

We would like the final flyer to have.
Side A : Yoga image, logo

Fennel Stretch Hall
address: 4/71 Wexcombe Lane, Pelharton
website: fennelstretch.com.au
mobile: 0471 296 814

Side B: Clear easy to read timetable with a break down of class types and website.

We would also like to have a copy of the timetable itself as a separate jpg or pdf for use on our website to download.

Thank you.
Yours kindly,
Nell

I have attached a sample of another timetable of which I like the look and feel of, however this is just a guide. I've also attached our 'new' schedule in WORD plus uploaded our last design of the front.
Updates

Target Market(s)

Women aged 30-45

Industry/Entity Type

Health And Wellness

Font styles to use
Other font styles liked:
• Brandon Grotesque, Jenna Sue

Colors
6c459b
33a6d7
ffffff

Requirements
Must have
• A definitive colour to decipher between different class types on our timetable. Where each colour represents a different class type. Colours and layouts similar to our website design, see www.fennelstretch.com.au
Nice to have
• I've included a design of another studio whose timetable design I like. One of our own yoga images instead of a stock image.
Should not have
• No dark gridlines between the cells/boxes in the timetables. Please don't use stock yoga images.

```html
<!DOCTYPE html>
<html lang="en">
<head>
<meta charset="utf-8">
<title>Fennel Stretch Hall – Spring Flyer</title>
<link rel="stylesheet" href="https://fonts.googleapis.com/css2?family=Josefin+Sans:wght@300;400;600&display=swap">
<style>
  :root {
    --backdrop: #3a3a3c;
    --brand-blue: #4a8fd6;
    --soft-blue: #5aa6de;
    --panel-blue: #5b8fcf;
    --head-blue: #6ccff6;
    --time-blue: #62c6f1;
    --empty: #f6f6f8;
    --ink: #222;
    --rise: #f7a08a;
    --vinyasa: #fff59a;
    --slow: #f1b4a7;
    --yin: #c9c9c9;
    --pregnancy: #b7d334;
    --mum: #fbb450;
    --kids: #f4a3c8;
    --teens: #a9dbe6;
    --flow-restore: #bfcfa2;
    --yin-restore: #9c9bd2;
    --wellness: #fdc88e;
  }
  * { box-sizing: border-box; margin: 0; padding: 0; }
  html, body { width: 918px; height: 1200px; overflow: hidden; }
  body {
    background: var(--backdrop);
    font-family: "Josefin Sans", sans-serif;
    position: relative;
  }

  /* Front side */
  .flyer-front {
    position: absolute; left: 80px; top: 70px;
    width: 741px; height: 523px;
    overflow: hidden;
  }
  .studio-photo {
    position: absolute; inset: 0;
    background:
      linear-gradient(180deg, #ffffff 0%, #fbfbfb 68%, #c89c6e 76%, #b0835a 88%, #9b7049 100%);
  }
  .studio-photo::after {
    content: ""; position: absolute; left: 110px; top: 150px; width: 470px; height: 280px;
    background: radial-gradient(ellipse at 55% 40%, rgba(108,69,155,.35), rgba(220,170,120,.25) 55%, transparent 72%);
  }
  .wordmark {
    position: absolute; left: 40px; top: 100px;
    font-weight: 400; font-size: 28px; letter-spacing: 9px;
    color: var(--brand-blue); text-transform: lowercase;
  }
  .tagline {
    position: absolute; left: 545px; top: 30px; width: 170px;
    text-align: center; font-weight: 300; font-size: 17px; line-height: 30px;
    color: var(--soft-blue);
  }
  .contact {
    position: absolute; left: 525px; top: 232px; width: 210px;
    text-align: center; font-size: 13px; line-height: 24px; color: #333;
  }
  .book-online {
    position: absolute; left: 373px; top: 421px; width: 113px; height: 30px;
    background: var(--brand-blue); color: #fff;
    font-size: 17px; line-height: 32px; text-align: center;
  }
  .web-address {
    position: absolute; left: 280px; top: 467px; width: 300px; text-align: center;
    color: #fff; font-weight: 600; font-size: 17px; letter-spacing: 1px;
  }

  /* Back side */
  .flyer-back {
    position: absolute; left: 80px; top: 622px;
    width: 741px; height: 522px;
    background: var(--panel-blue);
  }
  .timetable-title {
    position: absolute; left: 0; right: 0; top: 18px; text-align: center;
    color: #fff; font-size: 25px; letter-spacing: 4px; font-weight: 400;
  }
  .timetable-panel {
    position: absolute; left: 21px; top: 57px; width: 697px; height: 432px;
    background: #fff; padding: 4px 5px;
  }
  .timetable {
    display: grid;
    grid-template-columns: 52px 82px 84px 86px 116px 96px 84px 60px;
    grid-template-rows: 36px repeat(13, 26.5px);
    gap: 3.3px 4px;
    margin-left: 2px;
  }
  .timetable > div {
    display: flex; align-items: center; justify-content: center;
    font-size: 10.5px; color: var(--ink); text-transform: uppercase; white-space: nowrap;
    background: var(--empty);
  }
  .timetable .corner { background: transparent; }
  .timetable .day { background: var(--head-blue); color: #fff; font-size: 13.5px; }
  .timetable .time { background: var(--time-blue); text-transform: none; font-size: 10px; justify-content: flex-start; padding-left: 5px; }
  .rise { background: var(--rise) !important; }
  .vinyasa { background: var(--vinyasa) !important; }
  .slow { background: var(--slow) !important; }
  .yin { background: var(--yin) !important; }
  .pregnancy { background: var(--pregnancy) !important; }
  .mum { background: var(--mum) !important; }
  .kids { background: var(--kids) !important; }
  .teens { background: var(--teens) !important; }
  .flow-restore { background: var(--flow-restore) !important; }
  .yin-restore { background: var(--yin-restore) !important; }
  .wellness { background: var(--wellness) !important; }
  .footnote {
    position: absolute; left: 0; right: 0; top: 498px; text-align: center;
    color: #fff; font-size: 10px; letter-spacing: .5px;
  }
</style>
</head>
<body>

<section class="flyer-front">
  <div class="studio-photo" role="img" aria-label="Photo of a yoga student in downward dog pose on a sisal mat in the studio, with a faint mandala ornament behind the studio name"></div>
  <div class="wordmark">fennel stretch hall</div>
  <p class="tagline">Inclusive, Inspiring Boutique Yoga Studio Classes For All Ages + Abilities</p>
  <div class="contact">
    <p>4/71 Wexcombe Lane, Pelharton</p>
    <p>Mobile: 0471 296 814</p>
    <p>hello@fennelstretch.com.au</p>
  </div>
  <div class="book-online">book online</div>
  <div class="web-address">www.fennelstretch.com.au</div>
</section>

<section class="flyer-back">
  <h1 class="timetable-title">FENNEL STRETCH SPRING TIMETABLE</h1>
  <div class="timetable-panel">
    <div class="timetable">
      <div class="corner"></div>
      <div class="day">MONDAY</div><div class="day">TUESDAY</div><div class="day">WEDNESDAY</div><div class="day">THURSDAY</div><div class="day">FRIDAY</div><div class="day">SATURDAY</div><div class="day">SUNDAY</div>

      <div class="time">05.45 am</div><div></div><div class="rise">Rise + Shine*</div><div></div><div class="rise">Rise + Shine*</div><div></div><div></div><div></div>
      <div class="time">09.00 am</div><div></div><div></div><div></div><div></div><div></div><div class="vinyasa">Vinyasa Flow</div><div></div>
      <div class="time">09.15 am</div><div></div><div class="vinyasa">Vinyasa Flow</div><div></div><div></div><div></div><div></div><div></div>
      <div class="time">09.30 am</div><div class="slow">Slow Flow</div><div></div><div></div><div class="vinyasa">Vinyasa Flow</div><div></div><div></div><div class="yin">Yin</div>
      <div class="time">10.30 am</div><div></div><div></div><div></div><div></div><div></div><div class="pregnancy">Pregnancy*</div><div></div>
      <div class="time">11.00 am</div><div></div><div class="mum">Mum + Baby*</div><div></div><div class="mum">Mum + Baby*</div><div></div><div></div><div></div>
      <div class="time">12.15 pm</div><div></div><div></div><div></div><div class="pregnancy">Pregnancy</div><div></div><div></div><div></div>
      <div class="time">04.00 pm</div><div></div><div></div><div class="kids">Kids 8-12*</div><div class="kids">Kids 5- 7*</div><div></div><div class="vinyasa">Vinyasa Flow</div><div></div>
      <div class="time">04.45 pm</div><div></div><div></div><div class="teens">Teens12-16*</div><div></div><div></div><div></div><div></div>
      <div class="time">05.00 pm</div><div></div><div></div><div></div><div class="teens">Teens 12 – 16*</div><div></div><div></div><div></div>
      <div class="time">06.00 pm</div><div class="pregnancy">Pregnancy*</div><div class="vinyasa">Vinyasa Flow</div><div class="slow">Slow Flow</div><div></div><div class="flow-restore">Flow + Restore</div><div></div><div></div>
      <div class="time">06.15 pm</div><div></div><div></div><div></div><div class="pregnancy">Pregnancy*</div><div></div><div></div><div></div>
      <div class="time">07.30 pm</div><div class="vinyasa">Vinyasa Flow</div><div class="pregnancy">Pregnancy*</div><div class="yin-restore">Yin + Restore</div><div class="wellness">Women’s Wellness*</div><div></div><div></div><div></div>
    </div>
  </div>
  <p class="footnote">* bookings essential</p>
</section>

</body>
</html>
```